Casino with the 'highest winning percentage' needs a stationery design

This is for a casino in Colombo, Sri Lanka and we need a stationery design for business card, letter head and envelope.

Should be very professional, simple and elegant without fancy fonts

Reason: Not fully satisfied with the designs. Need more designs.

Industry/Entity Type

Business

Requirements
Must have
• 1. card deck symbol 'CLUBS' in red, or black

2. name in BLOCK CAPITAL LETTERS

3. Preferred font colours are black, white or red

4. Prefer 'professional /elegant' fonts
Should not have
• SHOULD NOT HAVE ANY OTHER SYMBOL EXCEPT 'CLUBS'

DO NOT PREFER ITALIC FONTS

```html
<!DOCTYPE html>
<html lang="en">
<head>
<meta charset="utf-8">
<title>Marlow's Entertainment – Business Card</title>
<link href="https://fonts.googleapis.com/css2?family=Exo+2:wght@400;500;600&display=swap" rel="stylesheet">
<style>
  :root {
    --backdrop: #d9d9d9;
    --card: #f7f7f7;
    --ink: #222222;
    --accent: #d9242b;
    --rule: #e0444a;
  }
  * { margin: 0; padding: 0; box-sizing: border-box; }
  html, body {
    width: 1200px; height: 900px; overflow: hidden;
    background: var(--backdrop);
    font-family: "Exo 2", sans-serif;
    color: var(--ink);
  }
  .card {
    position: absolute;
    left: 250px;
    width: 700px; height: 400px;
    background: var(--card);
    box-shadow: 0 6px 18px rgba(0,0,0,0.18);
  }
  .card--front { top: 40px; }
  .card--back { top: 470px; }

  /* Front */
  .brand-mark {
    position: absolute;
    left: 90px; top: 162px;
    width: 76px; height: 76px;
    border-radius: 50%;
    background: var(--accent);
  }
  .brand-name {
    position: absolute;
    left: 200px; top: 118px;
    font-weight: 600;
    font-size: 44px;
    line-height: 44px;
    letter-spacing: 2px;
    text-transform: uppercase;
    color: var(--ink);
  }
  .brand-rule {
    position: absolute;
    left: 200px; top: 230px;
    width: 440px; height: 2px;
    background: var(--rule);
  }
  .brand-region {
    position: absolute;
    left: 200px; top: 244px;
    font-weight: 600;
    font-size: 34px;
    letter-spacing: 2px;
    text-transform: uppercase;
    color: var(--ink);
  }

  /* Back */
  .back-mark {
    position: absolute;
    left: 100px; top: 50px;
    width: 80px; height: 80px;
    border-radius: 50%;
    background: var(--accent);
  }
  .address {
    position: absolute;
    left: 70px; top: 170px;
    font-size: 22px;
    line-height: 26px;
    font-style: normal;
  }
  .address .company { text-transform: uppercase; letter-spacing: 1px; }
  .contacts {
    position: absolute;
    left: 70px; top: 262px;
    font-size: 19px;
    line-height: 26px;
    letter-spacing: 0.5px;
  }
  .contacts .label { color: var(--accent); font-weight: 600; }
  .web {
    position: absolute;
    left: 70px; top: 330px;
    font-size: 19px;
    font-weight: 600;
    letter-spacing: 0.5px;
    color: var(--accent);
  }
</style>
</head>
<body>
  <section class="card card--front" aria-label="Business card front">
    <span class="brand-mark" aria-hidden="true"></span>
    <div class="brand-name">Marlow's<br>Entertainment</div>
    <span class="brand-rule" aria-hidden="true"></span>
    <div class="brand-region">Sri Lanka</div>
  </section>

  <section class="card card--back" aria-label="Business card back">
    <span class="back-mark" aria-hidden="true"></span>
    <address class="address">
      <span class="company">Marlow's Limited</span><br>
      18, Harbour View Mawatha<br>
      Colombo 01000, Sri Lanka
    </address>
    <div class="contacts">
      <span class="label">T</span>: + 94 11 5550142 | <span class="label">F</span>: + 94 11 0000000<br>
      <span class="label">M</span>: + 94 77 0000000 | <span class="label">E</span>: info@marlowscolombo.com
    </div>
    <div class="web">www.marlowscolombo.com</div>
  </section>
</body>
</html>
```